Oil and gas industry project solutions company needs professional cards with Canadian aboriginal fee

We are a aboriginally owned company that is focused on Project Planning, Management, Inspection & Consulting for Canada's Petroleum Industry. We have a logo that we would like to incorporate into a professional looking business card. We are professionals that offer services from project inception to completion.

Target Market(s)

Major industry leaders like NorthRidge Pipelines, Vantor, Kelstrand Energy, Brimwell etc.

Industry/Entity Type

Industry

Contact Information for Business Card

Reid Forbin
reid@kolbymarsh.ca
250 418 9067

Requirements
Must have
• KolbyMarsh Inc. logo.
• Address is: RR4, Site2, Comp7 Fort St. John, BC V1J 8K3 Traditional Territory of the Treaty 8 People
• Colors that are in logo
• Banner or picture on back
• Ability to put different names and contacts
• Website: kolbymarsh.ca
• "Project Planning, Management, Inspection & Consulting for Canada's Petroleum Industry"

```html
<!DOCTYPE html>
<html lang="en">
<head>
<meta charset="utf-8">
<title>KolbyMarsh Inc. Business Card</title>
<link rel="stylesheet" href="https://fonts.googleapis.com/css2?family=Source+Sans+3:wght@400;600;700&display=swap">
<style>
  :root {
    --navy: #1f2a6e;
    --green: #6ab446;
    --ink: #222222;
    --rule: #333333;
    --card: #ffffff;
    --backdrop: #e9e6e2;
  }
  * { margin: 0; padding: 0; box-sizing: border-box; }
  html, body { width: 1200px; height: 1000px; overflow: hidden; }
  body {
    background: var(--backdrop);
    font-family: "Source Sans 3", Arial, sans-serif;
    color: var(--ink);
    position: relative;
  }
  .card {
    position: absolute;
    left: 265px;
    width: 665px;
    height: 397px;
    background: var(--card);
    border-radius: 22px;
    overflow: hidden;
    box-shadow: 0 4px 14px rgba(0,0,0,0.18);
  }
  .card--front { top: 73px; }
  .card--back { top: 533px; }

  .brand {
    position: absolute;
    display: flex;
    align-items: center;
    gap: 12px;
  }
  .brand__dot {
    width: 22px; height: 22px;
    border-radius: 50%;
    background: var(--green);
    flex: none;
  }
  .brand__name {
    font-size: 40px;
    font-weight: 600;
    color: var(--navy);
    white-space: nowrap;
    letter-spacing: -0.3px;
  }
  .card--front .brand { left: 40px; top: 82px; }
  .card--back .brand { left: 300px; top: 280px; }

  .services {
    position: absolute;
    left: 38px; top: 170px;
    list-style: none;
    font-size: 17px;
    line-height: 22px;
  }
  .services li { position: relative; padding-left: 15px; }
  .services li::before {
    content: "";
    position: absolute; left: 0; top: 8px;
    width: 7px; height: 7px; border-radius: 50%;
    background: var(--green);
  }
  .holder-name {
    position: absolute;
    right: 32px; top: 232px;
    font-size: 22px; font-weight: 700;
    color: var(--navy);
    letter-spacing: 0.3px;
  }
  .divider {
    position: absolute;
    left: 32px; right: 32px; top: 271px;
    height: 1.5px; background: var(--rule);
  }
  .address {
    position: absolute;
    left: 34px; top: 301px;
    display: flex; gap: 6px;
    font-size: 17px; line-height: 22px;
    font-style: normal;
  }
  .address svg { flex: none; margin-top: 3px; }
  .contacts {
    position: absolute;
    right: 30px; top: 297px;
    list-style: none;
    font-size: 16px; line-height: 24.5px;
    text-align: right;
  }
  .contacts li { display: flex; justify-content: flex-end; align-items: center; gap: 7px; }
  .contacts svg { flex: none; }

  .back-photo {
    position: absolute; inset: 0;
    background:
      radial-gradient(ellipse at 55% 75%, rgba(200,190,175,0.55), transparent 60%),
      linear-gradient(180deg, #f3f3f2 0%, #e6e4e0 55%, #dcd8d2 100%);
  }
</style>
</head>
<body>
  <section class="card card--front">
    <div class="brand">
      <span class="brand__dot"></span>
      <span class="brand__name">KolbyMarsh Inc.</span>
    </div>

    <ul class="services">
      <li>Project Planning</li>
      <li>Management</li>
      <li>Inspection &amp; Consulting for<br>Canada's Petroleum Industry</li>
    </ul>

    <p class="holder-name">REID FORBIN</p>
    <div class="divider"></div>

    <address class="address">
      <svg width="12" height="17" viewBox="0 0 12 17" aria-hidden="true"><path d="M6 0C2.7 0 0 2.6 0 5.9 0 10.3 6 17 6 17s6-6.7 6-11.1C12 2.6 9.3 0 6 0zm0 8.2a2.3 2.3 0 1 1 0-4.6 2.3 2.3 0 0 1 0 4.6z" fill="var(--navy)"/></svg>
      <span>RR4, Site2, Comp7 Fort St. John,<br>BC V1J 8K3<br>Traditional Territory of the Treaty 8 People</span>
    </address>

    <ul class="contacts">
      <li>250 418 9067
        <svg width="15" height="12" viewBox="0 0 15 12" aria-hidden="true"><path d="M1 3.5C3 1 12 1 14 3.5l-.5 2-3-.5V3.8c-2-.6-4-.6-6 0V5l-3 .5z M3.5 6.5h8l1.5 5H2z" fill="var(--navy)"/></svg>
      </li>
      <li>reid@kolbymarsh.ca
        <svg width="15" height="11" viewBox="0 0 15 11" aria-hidden="true"><rect width="15" height="11" rx="1" fill="var(--navy)"/><path d="M1 1.5l6.5 5 6.5-5" stroke="#fff" stroke-width="1.2" fill="none"/></svg>
      </li>
      <li>www.kolbymarsh.ca
        <svg width="15" height="15" viewBox="0 0 15 15" aria-hidden="true"><circle cx="7.5" cy="7.5" r="6.5" fill="none" stroke="var(--navy)" stroke-width="1.6"/><path d="M1 7.5h13M7.5 1c-3 3.5-3 9.5 0 13M7.5 1c3 3.5 3 9.5 0 13" stroke="var(--navy)" stroke-width="1.2" fill="none"/></svg>
      </li>
    </ul>
  </section>

  <section class="card card--back">
    <div class="back-photo" role="img" aria-label="Faded photograph of pipeline workers in hard hats lowering a pipe section at a snowy construction site"></div>
    <div class="brand">
      <span class="brand__dot"></span>
      <span class="brand__name">KolbyMarsh Inc.</span>
    </div>
  </section>
</body>
</html>
```